Powerpoint template for trainer and coach in the field of personality development

Powerpoint template for coach and coach in the field of personality development I would like to have a basic design for Powerpoint 2007. It should work: clear, friendly, aesthetic, modern, simple, simple, beautiful, unique, at the same time warm and emotional ("masculine" in the settings seems to lead to rather cool designs). It's about aspects of personality development, psychology, human behavior, which of course has a lot to do with feelings. The lecture, which is based on the presentation, will also be more emotionally colored with objective background than the other. This personal level must be able to transport the design without being too flowery or playful or childish. (I know, maybe it's difficult :-) Charts and statistics are rather rare I would like a basic design for Powerpoint 2007. It should work: clear, friendly, friendly, aesthetic, modern, simple, simple, beautiful, clear, warm and emotional at the same time ("masculine" in the settings seems to lead to rather cool designs). It is about aspects of personality development, psychology and human behavior, which has a lot to do with feelings. So the presentation, which is based on the presentation, wants to be more emotionally colored with a factual background than the other way around. This personal level must be able to transport the design without appearing too flowery or playful or childlike. (I know, it may be difficult: -) Charts and statistics are rather rare Please refer to my previous CI: Logo Website: klaus-muecke. de Workshop-Flyer White as a background colored (red) bar top logo below small would be possible But I can imagine color as a basic background Make suggestions to your taste please and can not be restricted by my ideas The information on the color comes from mine previous agency, I hope you agree. In principle, elements can also be used in the following order: Word document template for handout - seminar materials or offer. Please contact me if you have any questions Best regards I would like a basic design for Powerpoint 2007. It should work: clear, friendly, aesthetic, modern, simple, simple, beautiful, clear Please refer to my previous CI: logo Website: klaus- Mücke. de workshop flyer White background (red) bar at the top of the page. Can you make a color change? The information on the color comes from my previous agency, I hope they are correct. In principle, elements can also be used in the following order: Word document template for handout - seminar materials or offer. With kind regards Color: Red CMYK: 15% Cyan 100% Magenta 100% Yellow 0% Black RGB Dec: 204, 7, 30 RGB%: 80 - 2.7 - 11.8

Target Market(s)

Personnel Developers - Managers -. Employees of companies Also from social enterprises and NGO Personnel developers - executives -. corporate employees So from social enterprises and NGOs

Font styles to use
Sans Serif

Colors
ec1f27

Requirements
Must have
• Title page incl. Logo content page text only: headline plus list No long texts. Only incrustations of max. 7 Punkte = Zeilen Content page Foto, beside Text (Aufzählung) Content page: Foto groß, on which several words as text Title page incl. Logo Content page only text: heading plus enumeration No long texts. Only enumerations of max. 7 points = lines Content page photo, next to it text (list) Contents page: photo large, on it several words as text
Nice to have
• Final page incl. QR code Final page including QR code
Should not have
• playfulness, very technical, cold, empirically oriented playful, very technical, cold, empirically oriented

```html
<!DOCTYPE html>
<html lang="en">
<head>
<meta charset="utf-8">
<title>Presentation template – content slides</title>
<link rel="stylesheet" href="https://fonts.googleapis.com/css2?family=Questrial&family=Josefin+Sans:wght@400;600&display=swap">
<style>
  :root {
    --brand-red: #c9151e;
    --brand-red-soft: #e89a9a;
    --photo-red-dark: #b5433d;
    --photo-red-light: #d9746b;
    --ink: #555555;
    --paper: #ffffff;
    --page: #ffffff;
    --shadow: rgba(0,0,0,0.35);
  }
  * { margin: 0; padding: 0; box-sizing: border-box; }
  html, body {
    width: 900px; height: 1200px; overflow: hidden;
    background: var(--page);
    font-family: "Questrial", "Century Gothic", sans-serif;
  }
  .canvas { position: relative; width: 900px; height: 1200px; }

  .slide {
    position: absolute; left: 30px; width: 842px; height: 473px;
    box-shadow: 2px 2px 3px var(--shadow);
    overflow: hidden;
  }

  /* list slide */
  .slide--list { top: 36px; background: var(--paper); border: 1px solid #eee; }
  .slide__brand {
    position: absolute; left: 24px; top: 33px;
    display: flex; align-items: center; gap: 10px;
    font-family: "Josefin Sans", sans-serif; font-weight: 600;
    font-size: 24px; letter-spacing: 0.5px; color: #333;
  }
  .slide__brand-square { width: 18px; height: 18px; background: var(--brand-red); }
  .slide__rule {
    position: absolute; left: 288px; top: 0; width: 1px; height: 100%;
    background: var(--brand-red);
  }
  .agenda { list-style: none; position: absolute; left: 283px; top: 132px; }
  .agenda__item {
    display: flex; align-items: center; height: 50px;
    font-size: 14.5px; color: var(--ink); letter-spacing: 0.2px;
  }
  .agenda__item::before {
    content: ""; width: 11px; height: 11px; background: var(--brand-red);
    margin-right: 13px;
  }
  .footer-name {
    position: absolute; left: 16px; top: 425px;
    font-family: "Questrial", sans-serif; font-size: 15px;
    letter-spacing: 1px; color: var(--brand-red);
  }
  .page-number {
    position: absolute; left: 784px; top: 428px;
    width: 18px; height: 18px; background: var(--brand-red);
    color: #fff; font-size: 8px; display: flex; align-items: center; justify-content: center;
  }

  /* photo slide */
  .slide--photo { top: 528px; }
  .slide__backdrop {
    position: absolute; inset: 0;
    background: linear-gradient(100deg, var(--photo-red-light) 0%, var(--photo-red-dark) 45%, #c4574e 70%, var(--photo-red-dark) 100%);
  }
  .slide__portrait {
    position: absolute; left: 435px; top: 76px; width: 321px; height: 321px;
    background: linear-gradient(160deg, #8d9094 0%, #5f6772 55%, #34405a 100%);
    box-shadow: 1px 2px 4px var(--shadow);
  }
  .slide__headline {
    position: absolute; right: 434px; top: 125px; text-align: right;
    font-family: "Questrial", sans-serif; font-weight: 400;
    font-size: 41px; line-height: 47px; color: #fff;
  }
  .slide__lead {
    position: absolute; right: 434px; top: 286px; text-align: right;
    font-size: 13px; line-height: 15px; color: #fff;
  }
  .slide__signature {
    position: absolute; left: 18px; top: 425px;
    display: flex; align-items: center; gap: 8px;
    font-family: "Questrial", sans-serif; font-size: 26px;
    letter-spacing: 1px; color: #fff;
  }
  .slide__signature-square { width: 9px; height: 9px; background: #fff; }
</style>
</head>
<body>
<main class="canvas">

  <section class="slide slide--list" aria-label="Agenda slide">
    <div class="slide__brand"><span class="slide__brand-square"></span>LOREM IPSUM</div>
    <div class="slide__rule"></div>
    <ul class="agenda">
      <li class="agenda__item">Lorem Ipsum Dolor Sit Amet</li>
      <li class="agenda__item">Lorem Ipsum Dolor Sit Amet</li>
      <li class="agenda__item">Lorem Ipsum Dolor Sit Amet</li>
      <li class="agenda__item">Lorem Ipsum Dolor Sit Amet</li>
      <li class="agenda__item">Lorem Ipsum Dolor Sit Amet</li>
      <li class="agenda__item">Lorem Ipsum Dolor Sit Amet</li>
    </ul>
    <div class="footer-name">KLAUS MÜCKE</div>
    <div class="page-number">2</div>
  </section>

  <section class="slide slide--photo" aria-label="Photo slide">
    <div class="slide__backdrop" role="img" aria-label="Red-tinted photo of the coach sitting on concrete stairs"></div>
    <div class="slide__portrait" role="img" aria-label="Portrait photo of the coach in a dark blazer sitting on grey steps"></div>
    <h2 class="slide__headline">Lorem Ipsum<br>Dolor Sit<br>Amet</h2>
    <p class="slide__lead">Lorem ipsum dolor sit amet, consetetur<br>sadipscing elitr, sed diam nonumy eirmod<br>tempor invidunt ut labore et dolore magna.</p>
    <div class="slide__signature"><span class="slide__signature-square"></span>KLAUS MÜCKE</div>
  </section>

</main>
</body>
</html>
```